Meadowbrook Clinical Trials Redesign

Website name: http://meadowbrookclinicaltrials.example/live/
Industry: medical & pharmaceutical
Target audience:
Clinical research patients
clinical research sponsors
clinical research referring doctors
Style/theme of your website design:
We want to customize the corvid theme, emulating our competitors website
http://layoutbazaar.example/item/corvid-responsive-multipurpose-wordpress-theme/4172305
Webdesign Examples?
http://www.jpnclinical.example/currently-enrolling-clinical-trials/
https://www.tundrastudies.example/
What do you like about these sites:
These sites address all the needs of a clinical trial facility. The patient, the doctor and the sponsor. Also they have forms and sign up information for each trial they offer. The site needs to have SCHEMA markup and rich snippets. We have reviews and testimonial that need schema markup also, local NAP information and all the other rich snippet markups available.
How many pages need design:
8-12
List any colors:
existing color of website and logo
Target Market(s)
Target audience:
Industry/Entity Type
Pharmaceutical
Number of Pages Required
5+ page

```html
<!DOCTYPE html>
<html lang="en">
<head>
<meta charset="utf-8">
<title>Meadowbrook Clinical Trials</title>
<link href="https://fonts.googleapis.com/css2?family=Roboto:wght@300;400;500&display=swap" rel="stylesheet">
<style>
:root{
  --blue:#0e7cc0;
  --green:#6fc21c;
  --orange:#fd8a07;
  --charcoal:#3a3a3a;
  --text:#333;
  --muted:#8b8b8b;
  --line:#e3e3e3;
  --footer:#2d2d2d;
  --footer-deep:#1f1f1f;
  --footer-text:#a9a9a9;
  --white:#fff;
}
*{margin:0;padding:0;box-sizing:border-box}
html,body{width:1200px;height:2308px;overflow:hidden;background:var(--white)}
body{position:relative;font-family:'Roboto',Arial,sans-serif;font-weight:300;color:var(--text)}
.abs{position:absolute}
a{color:inherit;text-decoration:none}

/* header */
.brand{left:59px;top:24px;display:flex;align-items:center;gap:14px}
.brand-mark{width:40px;height:40px;border-radius:50%;background:var(--blue)}
.brand-name{font-size:27px;line-height:27px;font-weight:400;color:var(--blue);width:170px}
.contact-line{right:54px;top:26px;display:flex;gap:28px;font-size:13px;color:#555;font-weight:400}
.contact-line span{display:flex;align-items:center;gap:8px}
.social{right:54px;top:58px;display:flex;gap:8px}
.social i{display:block;width:26px;height:26px;border:1px solid #ddd;background:#f6f6f6}

/* nav */
.nav{left:57px;top:120px;width:1089px;height:50px;border:1px solid var(--line);display:flex;font-size:13px;font-weight:400}
.nav a{display:flex;align-items:center;padding:0 26px;border-right:1px solid var(--line);color:#444;letter-spacing:.3px}
.nav a.active{background:var(--blue);color:var(--white);padding:0 38px}
.nav .search{margin-left:auto;width:53px;background:var(--blue);display:flex;align-items:center;justify-content:center}

/* hero */
.hero{left:0;top:199px;width:1200px;height:395px;background:linear-gradient(100deg,#eef3f7 0%,#dfe8ef 35%,#e8cbb6 55%,#c99f86 75%,#dfe5ea 100%)}
.hero-card{left:59px;top:252px;width:466px;height:184px;background:rgba(255,255,255,.55);padding:24px 30px}
.hero-card h2{font-weight:300;font-size:31px;color:#444;line-height:34px}
.hero-card h1{font-weight:300;font-size:46px;color:var(--blue);line-height:52px}
.hero-card p{font-size:14px;color:#8a8a8a;margin-top:14px;line-height:20px}

/* feature tiles */
.tiles{left:57px;top:594px;width:1089px;height:252px;display:flex}
.tile{flex:1;color:var(--white);padding:22px 28px}
.tile h3{font-weight:300;font-size:29px;line-height:30px;height:70px}
.tile p{font-size:12.5px;line-height:20px;font-weight:400;margin-top:4px;height:90px}
.tile .more{font-size:12.5px;font-weight:400;display:block;margin-top:10px}
.tile.serv{background:var(--blue)}
.tile.book{background:var(--green)}
.tile.rand{background:var(--orange)}
.tile.rand h3{font-size:27px;line-height:26px}
.tile.hours{background:var(--charcoal)}
.hours-row{display:flex;justify-content:space-between;font-size:12.5px;font-weight:400;padding:10px 0;border-bottom:1px solid #555}
.hours-row:last-child{border:0}

/* welcome */
.welcome-title{left:0;width:1200px;top:888px;text-align:center;font-size:30px;font-weight:400;color:var(--blue)}
.welcome-text{left:0;width:1200px;top:950px;text-align:center;font-size:17px;line-height:25px;color:#7a7a7a}
.services{left:57px;top:1062px;width:1089px;display:flex}
.service{flex:1;text-align:center;padding:0 14px}
.service svg{display:block;margin:0 auto}
.service h4{font-weight:400;font-size:20px;color:#333;margin-top:16px}
.service p{font-size:12.5px;line-height:19px;color:var(--muted);margin-top:12px}
.divider{left:57px;top:1291px;width:1089px;height:1px;background:var(--line)}
.divider::before{content:"";position:absolute;left:0;top:-1px;width:234px;height:3px;background:var(--blue)}

/* news & testimonials */
.section-title{font-size:20px;font-weight:400;color:#333;padding-bottom:14px;border-bottom:1px solid var(--line);position:absolute}
.section-title::after{content:"";position:absolute;left:0;bottom:-2px;width:40px;height:3px;background:var(--blue)}
.news-title{left:57px;top:1356px;width:524px}
.testi-title{left:621px;top:1356px;width:525px}
.pager{right:54px;top:1354px;display:flex;gap:4px}
.pager i{display:flex;width:22px;height:22px;border:1px solid #ddd;align-items:center;justify-content:center}
.pager i.on{background:var(--blue);border-color:var(--blue)}
.news-item{left:57px;width:524px;display:flex;gap:24px}
.news-thumb{width:126px;height:120px;flex:none}
.news-item h5{font-size:19px;font-weight:400;color:var(--blue)}
.news-item .meta{font-size:11px;color:var(--muted);margin-top:6px}
.news-item .meta b{font-weight:300;color:var(--blue)}
.news-item p{font-size:12.5px;line-height:19px;color:var(--muted);margin-top:10px}
.quote-box{left:621px;top:1448px;width:525px;height:172px;border:1px solid #ddd;padding:28px 32px 0 84px;font-size:13px;line-height:22px;color:var(--muted)}
.quote-box::after{content:"";position:absolute;left:24px;bottom:-12px;width:22px;height:22px;background:var(--white);border-right:1px solid #ddd;border-bottom:1px solid #ddd;transform:rotate(45deg)}
.qmark{width:32px;height:32px;background:var(--blue);display:flex;align-items:center;justify-content:center}
.author{left:621px;top:1647px;display:flex;gap:20px;align-items:center}
.avatar{width:57px;height:57px;background:#e3e3e3}
.author strong{display:block;font-size:14px;font-weight:400;color:#333}
.author em{font-style:normal;font-size:12px;color:var(--blue)}

/* tweet band */
.tweet-band{left:0;top:1773px;width:1200px;height:63px;background:var(--blue);color:var(--white);display:flex;align-items:center;padding:0 57px;font-size:13px;font-weight:400}
.tweet-band .dot{width:22px;height:22px;border-radius:50%;background:var(--white);margin-right:40px}
.tweet-band .arrows{margin-left:auto;display:flex;gap:4px}
.tweet-band .arrows i{width:22px;height:22px;border:1px solid rgba(255,255,255,.7);display:flex;align-items:center;justify-content:center}

/* footer */
.footer{left:0;top:1836px;width:1200px;height:419px;background:var(--footer)}
.fcol{position:absolute;top:1870px;color:var(--footer-text);font-size:12.5px;line-height:19px}
.fcol h6{font-size:17px;font-weight:400;color:var(--white);padding-bottom:14px;position:relative;margin-bottom:30px}
.fcol h6::after{content:"";position:absolute;left:0;bottom:0;width:40px;height:2px;background:var(--blue)}
.finfo{display:flex;gap:18px;margin-top:18px;color:#ddd}
.finfo svg{flex:none;margin-top:2px}
.fimg{width:245px;height:150px;background:linear-gradient(135deg,#1a4c6e,#2e86b8 55%,#5fb4d8)}
.fcol .cap{color:var(--white);margin-top:10px;font-size:13px}
.flinks li{list-style:none;color:#e6e6e6;font-size:12px;font-weight:400;margin-bottom:14px}
.flinks li::before{content:"›";color:#888;margin-right:8px}
.form label{display:block;font-size:12px;color:#ccc;margin-bottom:8px}
.form .field{border:1px solid #555;background:#2a2a2a;width:244px;height:34px;margin-bottom:18px}
.form .area{height:103px}
.form .btn{display:inline-block;background:var(--white);color:#333;font-size:12px;font-weight:400;padding:8px 20px;margin-top:6px}
.fpager{left:537px;top:1870px;display:flex;gap:2px}
.fpager i{width:22px;height:22px;background:#444;display:flex;align-items:center;justify-content:center}
.fpager i.on{background:var(--white)}
.copyright{left:0;top:2255px;width:1200px;height:53px;background:var(--footer-deep);color:#ddd;font-size:16px;font-weight:400;display:flex;align-items:center;padding-left:57px}
</style>
</head>
<body>

<header>
  <div class="abs brand"><span class="brand-mark"></span><span class="brand-name">Meadowbrook Clinical Trials</span></div>
  <div class="abs contact-line">
    <span><svg width="10" height="14" viewBox="0 0 10 14"><rect x="1" y="0.5" width="8" height="13" rx="1.5" fill="none" stroke="#0e7cc0"/><circle cx="5" cy="11" r="1" fill="#0e7cc0"/></svg>Call us: 1-800-555-0142</span>
    <span><svg width="14" height="10" viewBox="0 0 14 10"><rect x=".5" y=".5" width="13" height="9" fill="#0e7cc0"/><path d="M.5 .5 7 5.5 13.5 .5" fill="none" stroke="#fff"/></svg>contact@meadowbrookclinical.example</span>
  </div>
  <div class="abs social"><i></i><i></i><i></i><i></i><i></i></div>
</header>

<nav class="abs nav">
  <a class="active" href="#">HOME</a>
  <a href="#">ABOUT US</a>
  <a href="#">USER SUPPORT</a>
  <a href="#">CONTACTS</a>
  <span class="search"><svg width="16" height="16" viewBox="0 0 16 16"><circle cx="6.5" cy="6.5" r="5" fill="none" stroke="#fff" stroke-width="2"/><path d="M10 10l5 5" stroke="#fff" stroke-width="2.4"/></svg></span>
</nav>

<section class="abs hero" role="img" aria-label="Photo of a caregiver's hands gently holding an elderly patient's hand"></section>
<div class="abs hero-card">
  <h2>We Care About</h2>
  <h1>Every Client</h1>
  <p>Cum sociis natoque penatibus et magnis dis parturient montesmus. Pro vel nibh et elit mollis commodo et nec augue tristique sed.</p>
</div>

<section class="abs tiles">
  <div class="tile serv">
    <h3>TrialServ™</h3>
    <p>TrialServ™ is a contract clinical label generation service that provides you with ready to apply clinical labels specifically...</p>
    <a class="more" href="#">Read More</a>
  </div>
  <div class="tile book">
    <h3>TrialBook™</h3>
    <p>TrialBook™ labels are multi-page clinical labels used to address the needs of multi-language studies. This enables user to prepare...</p>
    <a class="more" href="#">Read More</a>
  </div>
  <div class="tile rand">
    <h3>Clinical Randomizations</h3>
    <p>Our systems can create randomization data for all types of CTM requirements. Patient randomization, material randomization and random...</p>
    <a class="more" href="#">Read More</a>
  </div>
  <div class="tile hours">
    <h3>Opening Hours</h3>
    <div class="hours-row"><span>Monday - Friday</span><span>8.00 - 17.00</span></div>
    <div class="hours-row"><span>Saturday</span><span>9.30 - 17.30</span></div>
    <div class="hours-row"><span>Sunday</span><span>9.30 - 15.00</span></div>
  </div>
</section>

<h2 class="abs welcome-title">Welcome to Meadowbrook Clinical Trials</h2>
<p class="abs welcome-text">Brookline Clinical Systems specializes in providing products and services to the pharmaceutical industry.<br>We are focused on the needs of those individuals involved with Clinical Trial Materials.<br>Our products and services are summarized below:</p>

<section class="abs services">
  <div class="service">
    <svg width="52" height="46" viewBox="0 0 52 46"><path d="M26 44 6 24C-1 17 3 4 13 4c6 0 10 4 13 8 3-4 7-8 13-8 10 0 14 13 7 20z" fill="none" stroke="#0e7cc0" stroke-width="4"/><path d="M8 24h12l4-8 5 14 4-6h11" fill="none" stroke="#0e7cc0" stroke-width="3"/></svg>
    <h4>TrialPro/LBL™</h4>
    <p>Cum sociis natoque penatibus et magnis dis parturient montesmus. Pro vel nibh et elit mollis commodo et nec augueique</p>
  </div>
  <div class="service">
    <svg width="52" height="46" viewBox="0 0 52 46"><g transform="rotate(-45 26 23)"><rect x="6" y="14" width="40" height="18" rx="9" fill="none" stroke="#0e7cc0" stroke-width="4"/><path d="M26 14v18" stroke="#0e7cc0" stroke-width="4"/></g></svg>
    <h4>Software Validation Services</h4>
    <p>Cum sociis natoque penatibus et magnis dis parturient montesmus. Pro vel nibh et elit mollis commodo et nec augueique</p>
  </div>
  <div class="service">
    <svg width="52" height="46" viewBox="0 0 52 46"><rect x="18" y="4" width="16" height="8" fill="none" stroke="#fd8a07" stroke-width="3"/><rect x="4" y="10" width="44" height="32" rx="3" fill="#fd8a07"/><path d="M26 17v18M17 26h18" stroke="#fff" stroke-width="5"/></svg>
    <h4>Clinical Label Stock</h4>
    <p>Cum sociis natoque penatibus et magnis dis parturient montesmus. Pro vel nibh et elit mollis commodo et nec augueique</p>
  </div>
  <div class="service">
    <svg width="52" height="46" viewBox="0 0 52 46"><circle cx="26" cy="15" r="11" fill="#0e7cc0"/><path d="M8 44c0-11 8-17 18-17s18 6 18 17z" fill="#0e7cc0"/></svg>
    <h4>Qualified Doctors</h4>
    <p>Cum sociis natoque penatibus et magnis dis parturient montesmus. Pro vel nibh et elit mollis commodo et nec augueique</p>
  </div>
</section>
<div class="abs divider"></div>

<h3 class="section-title news-title">Latest News</h3>
<article class="abs news-item" style="top:1443px">
  <div class="news-thumb" role="img" aria-label="Photo of medical equipment on a doctor's desk" style="background:linear-gradient(135deg,#cfe3f1,#6fa9d2 60%,#e6eef4)"></div>
  <div>
    <h5>Young women having her neck pain checked</h5>
    <div class="meta">September 15, 2013 &nbsp; <b>Comments (4)</b></div>
    <p>Cum sociis natoque penatibus et magnis dis parturient montesmus. Pro vel nibh et elit mollis commodo et nec augueique Mauris at justo eu lectus auctor porta vel ut libero.</p>
  </div>
</article>
<article class="abs news-item" style="top:1584px">
  <div class="news-thumb" role="img" aria-label="Photo of a medical monitoring device" style="background:linear-gradient(135deg,#f2f2f2,#c9ccd0 60%,#9aa1a8)"></div>
  <div>
    <h5>Medical Equipment</h5>
    <div class="meta">September 15, 2013 &nbsp; <b>Comments (2)</b></div>
    <p>Cum sociis natoque penatibus et magnis dis parturient montesmus. Pro vel nibh et elit mollis commodo et nec augueique Mauris at justo eu lectus auctor porta vel ut libero.</p>
  </div>
</article>

<h3 class="section-title testi-title">Testimonials</h3>
<div class="abs pager">
  <i><svg width="6" height="8" viewBox="0 0 6 8"><path d="M5 0 1 4l4 4" fill="none" stroke="#aaa"/></svg></i>
  <i class="on"><svg width="6" height="8" viewBox="0 0 6 8"><path d="M1 0l4 4-4 4" fill="#fff"/></svg></i>
</div>
<blockquote class="abs quote-box">
  <span class="qmark abs" style="left:24px;top:20px"><svg width="16" height="12" viewBox="0 0 16 12"><path d="M0 12V6l3-6h3L4 6h3v6zm9 0V6l3-6h3l-2 6h3v6z" fill="#fff"/></svg></span>
  Cum sociis natoque penatibus et magnis dis parturient esmus. Pro vel nibh et elit mollis commodo et nec augueique Mauris at justo eu lectus auctor porta vel ut libero. Suspe mattis tellus vel augue mollis ultrices. Suspendisse poten.
  <span class="qmark abs" style="left:320px;top:104px"><svg width="16" height="12" viewBox="0 0 16 12"><path d="M16 0v6l-3 6h-3l2-6H9V0zM7 0v6l-3 6H1l2-6H0V0z" fill="#fff"/></svg></span>
</blockquote>
<div class="abs author">
  <div class="avatar" role="img" aria-label="Portrait of the reviewer"></div>
  <div><strong>Elena Hartwell</strong><em>Our Psychologist</em></div>
</div>

<div class="abs tweet-band">
  <span class="dot"></span>
  Cum sociis natoque penatibus et magnis dis parturient montesmus. Pro vel nibh et elit mollis commodo et nec augueique Mauris at justo eu lectus
  <span class="arrows">
    <i><svg width="6" height="8" viewBox="0 0 6 8"><path d="M5 0 1 4l4 4" fill="#fff"/></svg></i>
    <i><svg width="6" height="8" viewBox="0 0 6 8"><path d="M1 0l4 4-4 4" fill="#fff"/></svg></i>
  </span>
</div>

<footer>
  <div class="abs footer"></div>
  <div class="fcol" style="left:57px;width:240px">
    <h6>Brookline Clinical Systems</h6>
    <p>Cum sociis natoque penatibus et magnis dis parturient montesmus. Pro vel nibh et elit mollis commodo et nec augueique</p>
    <div class="finfo" style="margin-top:34px"><svg width="12" height="16" viewBox="0 0 12 16"><path d="M6 16S0 9 0 6a6 6 0 0 1 12 0c0 3-6 10-6 10z" fill="#0e7cc0"/><circle cx="6" cy="6" r="2" fill="#2d2d2d"/></svg><span>Brookline Clinical Systems<br>Street Name 123<br>123 45 Cityname</span></div>
    <div class="finfo"><svg width="12" height="16" viewBox="0 0 12 16"><rect x="1" y="1" width="10" height="14" rx="1.5" fill="#0e7cc0"/></svg><span>+123 900 555 018</span></div>
    <div class="finfo"><svg width="14" height="10" viewBox="0 0 14 10"><rect width="14" height="10" fill="#0e7cc0"/><path d="M0 0l7 5 7-5" fill="none" stroke="#2d2d2d"/></svg><span style="color:#fff">info@meadowbrookclinical.example</span></div>
  </div>
  <div class="fcol" style="left:338px;width:250px">
    <h6>Services</h6>
    <div class="fimg" role="img" aria-label="Illustration of a hand touching a grid of medical icons"></div>
    <div class="cap">Accurate analyzes</div>
    <p style="margin-top:8px">Cum sociis natoque penatibus et magnis dis parturient montesmus. Pro vel nibh et elit</p>
  </div>
  <div class="abs fpager">
    <i><svg width="6" height="8" viewBox="0 0 6 8"><path d="M5 0 1 4l4 4" fill="#aaa"/></svg></i>
    <i class="on"><svg width="6" height="8" viewBox="0 0 6 8"><path d="M1 0l4 4-4 4" fill="#333"/></svg></i>
  </div>
  <div class="fcol" style="left:621px;width:240px">
    <h6>Doctors</h6>
    <ul class="flinks">
      <li>Careers</li><li>Company news</li><li>Investor relations</li><li>Site map</li><li>Community</li><li>Gallery</li><li>Updates</li><li>Videos</li>
    </ul>
  </div>
  <div class="fcol form" style="left:902px;width:250px">
    <h6>Quick Contacts</h6>
    <label>Your Email</label><div class="field"></div>
    <label>Your Email</label><div class="field area"></div>
    <span class="btn">Submit</span>
  </div>
  <div class="abs copyright">copyright 2015 Meadowbrook clinical, All right Reserved.</div>
</footer>

</body>
</html>
```